Book Cover for Fitness Trainer for Men

My name is Mabel Joy Crane. I am a female Fitness Trainer for Men.
I need a new Book Cover Design for my second book and a back of the book.
Both with updated text.
#A… Book Cover… I like the bright red and yellow colors.
I like the weight rack and the bold headline Font
#B… Book Cover…I like the full frontal sexier body. I don not like the font style.
I want the new design sexier; super sexy. Even more eye catching for guys.
I want to push the envelope to the point of almost too much sexy.
An Brindlo book 6”x9”, 150 pages

Target Market(s)

Men

Industry/Entity Type

Health and fitness for men

Colors
FFF300
FFF600
FEFA6F
FFFEC7
FFFEE8
EB3D1F
EC4F4E
F09395
F8D3D4
FCEDEE

Requirements
Must have
• Sexy & eye catching.

```html
<!DOCTYPE html>
<html lang="en">
<head>
<meta charset="utf-8">
<title>Fitness Trainer for Men – Book Cover</title>
<link rel="stylesheet" href="https://fonts.googleapis.com/css2?family=Open+Sans:wdth,wght@75..100,300..800&family=Dancing+Script:wght@700&display=swap">
<style>
  :root {
    --page-bg: #e4e4e4;
    --ink: #131313;
    --back-bg: #141414;
    --mat-light: #3a3a3a;
    --mat-dark: #1a1a1a;
    --gold: #f4b323;
    --white: #ffffff;
    --red: #c8301d;
    --sky: #3e93d6;
    --pool: #2fa6cf;
    --skin-dark: #2e1f17;
    --skin-mid: #7a513a;
  }
  * { margin: 0; padding: 0; box-sizing: border-box; }
  html, body { width: 1200px; height: 990px; overflow: hidden; }
  body {
    background: var(--page-bg);
    font-family: "Open Sans", sans-serif;
    font-stretch: 75%;
    position: relative;
  }
  .cover {
    position: absolute;
    left: 40px; top: 95px;
    width: 1120px; height: 800px;
    background: var(--back-bg);
    overflow: hidden;
  }

  /* ---------- back cover ---------- */
  .back { position: absolute; left: 0; top: 0; width: 536px; height: 800px; color: var(--white); }
  .back-mat {
    position: absolute; left: 430px; top: 0; width: 106px; height: 800px;
    background:
      radial-gradient(ellipse 80px 260px at 70% 20%, rgba(90,90,90,0.55), transparent 70%),
      radial-gradient(ellipse 80px 220px at 40% 75%, rgba(80,80,80,0.45), transparent 70%),
      linear-gradient(180deg, var(--mat-light) 0%, var(--mat-dark) 55%, #2c2c2c 100%);
  }
  .back-title {
    position: absolute; top: 41px; left: 74px; height: 30px; width: 400px;
    font-weight: 700; font-size: 26px; line-height: 30px; letter-spacing: 0.2px;
  }
  .back-title span { position: absolute; top: 0; height: 30px; white-space: nowrap; }
  .back-title .tag { background: var(--gold); color: var(--ink); text-align: center; }
  .back-title .t-fitness { left: 0; width: 113px; }
  .back-title .t-trainer { left: 126px; color: var(--white); }
  .back-title .t-men { left: 221px; width: 93px; }
  .back-title small { font-size: 15px; margin-right: 4px; }

  .copy { position: absolute; left: 74px; white-space: nowrap; }
  .copy-body { font-size: 10.6px; line-height: 17.3px; font-weight: 400; }
  .copy-lead { font-size: 13.5px; line-height: 17.6px; font-weight: 500; }
  .copy-quote { font-size: 10.8px; line-height: 17.5px; font-style: italic; font-weight: 400; }
  .copy-gold { color: var(--gold); }
  .section-head {
    position: absolute; left: 74px; top: 449px; width: 214px;
    font-size: 14.5px; line-height: 18px; font-weight: 500;
    padding-bottom: 7px; border-bottom: 1px solid var(--red);
  }

  .author-photo {
    position: absolute; left: 358px; top: 331px; width: 148px; height: 170px;
    background:
      radial-gradient(ellipse 50px 62px at 55% 42%, rgba(214,168,132,0.9), transparent 75%),
      linear-gradient(160deg, #e3ddd6 0%, #b98b66 50%, #3f5e5a 100%);
  }
  .author-caption {
    position: absolute; left: 358px; top: 505px; width: 113px; height: 53px;
    background: var(--ink); padding-top: 8px;
  }
  .author-caption .name { font-size: 13.5px; line-height: 17px; font-weight: 500; }
  .author-caption .role { font-size: 9.6px; line-height: 14px; font-weight: 400; }
  .mission { left: 358px; font-size: 9.8px; line-height: 17.3px; }
  .back-dumbbell {
    position: absolute; left: 403px; top: 127px; width: 102px; height: 57px;
    background: radial-gradient(ellipse at center, rgba(110,110,110,0.7) 0%, rgba(40,40,40,0.6) 55%, transparent 75%);
  }

  /* ---------- spine ---------- */
  .spine {
    position: absolute; left: 536px; top: 0; width: 51px; height: 800px;
    background: var(--gold);
  }
  .spine-text {
    position: absolute; left: 50%; white-space: nowrap;
    font-weight: 700; font-size: 24px; color: var(--ink);
    transform-origin: center; transform: translate(-50%, -50%) rotate(-90deg);
  }
  .spine-text small { font-size: 17px; }
  .spine-title { top: 490px; }
  .spine-author { top: 248px; font-size: 22px; }

  /* ---------- front cover ---------- */
  .front { position: absolute; left: 587px; top: 0; width: 533px; height: 800px; }
  .front svg { display: block; width: 533px; height: 800px; }
  .front .title { font-family: "Open Sans", sans-serif; font-stretch: 75%; font-weight: 700; fill: var(--ink); }
  .front .title-xb { font-weight: 800; }
  .front .author { font-family: "Open Sans", sans-serif; font-stretch: 75%; font-weight: 500; fill: var(--white); font-size: 33px; }
  .front .script { font-family: "Dancing Script", cursive; font-weight: 700; }
  .front .benefit { font-family: "Open Sans", sans-serif; font-stretch: 75%; font-weight: 500; font-size: 22.5px; fill: var(--white); }
</style>
</head>
<body>
<main class="cover">

  <section class="back">
    <div class="back-mat" role="img" aria-label="Dark rubber gym floor mat texture"></div>

    <h2 class="back-title">
      <span class="tag t-fitness">FITNESS</span>
      <span class="t-trainer">TRAINER</span>
      <span class="tag t-men"><small>for</small>MEN</span>
    </h2>

    <p class="copy copy-body" style="top:91px">I’ve been using eye candy to get guys interested in health and fitness since the<br>day I walked in the gym and turned heads.&nbsp; I figured if you wanted Tits &amp; Ass I’d<br>give it to you.&nbsp; Enough to make a buck and get my guys healthier. As a personal<br>fitness trainer for Men I’ve learned...that not all Guys are the same.&nbsp; Each of you<br>is different and You need to find what works for You.&nbsp; When you do ... the the<br>pounds melt away, your gut shrinks, and your health improves.</p>

    <p class="copy copy-lead" style="top:216px">You’ll love the new you.&nbsp; Your girl friend will love it. Your wife will love it.<br>Nothing a woman loves more than a long rock hard man in shape.</p>

    <p class="copy copy-body" style="top:269.5px">While everybody in the fitness community screams and yells about<br>gym memberships, 30 day challenges, and complete diet changes ...<br>My Guys don’t do all that.&nbsp; My Guys are Real Men with Real bodies.<br>Real Men that work for a living and don’t have time to live in the<br>gym.</p>

    <p class="copy copy-body" style="top:373px">Real men are tired of gym rats with “Look at me” egos, God given<br>1% body fat and abs you’ll never get.&nbsp; These guys are full of Shit!<br>And they’re the first one to buy my book.&nbsp; Ya gotta love it.</p>

    <h3 class="section-head">You need to find what works for you.</h3>

    <p class="copy copy-quote" style="top:494px">“I made a few adjustment in my meals added a minimum amount<br>of exercise and lost 17 pounds in three months.&nbsp; Thanks Mabel.<br>Couldn’t have done it without you.”</p>

    <p class="copy copy-quote" style="top:565px">“Mabel I took your bait and it actually made sense. Can’t believe<br>you got me exercising. My gut shrunk and had to buy new pants.<br>Best 20 bucks I ever spent.”</p>

    <p class="copy copy-lead" style="top:647px">Real Men can be fit, healthy and in shape no<br>matter their size, weight, or body fat.</p>

    <p class="copy copy-lead copy-gold" style="top:709px">Think you can do Twenty bucks to Get You<br>Hot, Sweaty, and Hard?</p>

    <div class="back-dumbbell" role="img" aria-label="Black iron dumbbell"></div>
    <div class="author-photo" role="img" aria-label="Portrait photo of the author Mabel Joy Crane"></div>
    <div class="author-caption">
      <p class="name">Mabel Joy Crane</p>
      <p class="role">Fitness Trainer for Men</p>
    </div>
    <p class="copy copy-body mission" style="top:565px">My mission is to get your lazy ass in<br>shape by finding what works for<br>you.&nbsp; If I need to get your attention<br>first...Then that’s what I’ll do.</p>
  </section>

  <section class="spine">
    <p class="spine-text spine-author">MABEL JOY CRANE</p>
    <p class="spine-text spine-title">FITNESS TRAINER <small>for</small> MEN</p>
  </section>

  <section class="front">
    <svg viewBox="0 0 533 800" xmlns="http://www.w3.org/2000/svg">
      <defs>
        <linearGradient id="torso-tone" x1="0" y1="0" x2="0" y2="1">
          <stop offset="0" stop-color="#151515"/>
          <stop offset="0.12" stop-color="#1b1613"/>
          <stop offset="0.2" stop-color="var(--skin-dark)"/>
          <stop offset="0.42" stop-color="#4a3326"/>
          <stop offset="0.6" stop-color="var(--skin-dark)"/>
          <stop offset="0.7" stop-color="#141414"/>
          <stop offset="1" stop-color="#121212"/>
        </linearGradient>
        <radialGradient id="torso-glow" cx="0.5" cy="0.5" r="0.5">
          <stop offset="0" stop-color="var(--skin-mid)" stop-opacity="0.9"/>
          <stop offset="1" stop-color="var(--skin-dark)" stop-opacity="0"/>
        </radialGradient>
        <linearGradient id="pool-tone" x1="0" y1="0" x2="0" y2="1">
          <stop offset="0" stop-color="#4aa6e0"/>
          <stop offset="1" stop-color="var(--pool)"/>
        </linearGradient>
        <radialGradient id="bather-tone" cx="0.5" cy="0.45" r="0.5">
          <stop offset="0" stop-color="#e9cfb4" stop-opacity="0.95"/>
          <stop offset="0.6" stop-color="#d8b48f" stop-opacity="0.6"/>
          <stop offset="1" stop-color="#d8b48f" stop-opacity="0"/>
        </radialGradient>
        <radialGradient id="iron-tone" cx="0.5" cy="0.5" r="0.5">
          <stop offset="0" stop-color="#8a8a8a" stop-opacity="0.85"/>
          <stop offset="0.6" stop-color="#3a3a3a" stop-opacity="0.7"/>
          <stop offset="1" stop-color="#222" stop-opacity="0"/>
        </radialGradient>
      </defs>

      <g role="img" aria-label="Photo of a sweaty toned female midriff in black sportswear">
        <rect x="0" y="0" width="533" height="800" fill="url(#torso-tone)"/>
        <ellipse cx="190" cy="300" rx="200" ry="200" fill="url(#torso-glow)"/>
      </g>

      <polygon points="272,0 406,0 239,111" fill="var(--sky)"/>
      <polygon points="406,0 533,0 533,359 360,470 239,111" fill="var(--gold)"/>
      <polygon role="img" aria-label="Photo of a swimming pool" points="533,359 533,640 470,707 360,707 336,475" fill="url(#pool-tone)"/>
      <rect x="0" y="707" width="533" height="93" fill="var(--ink)"/>
      <polygon role="img" aria-label="Dark rubber gym floor mat texture" points="0,640 150,670 150,800 0,800" fill="#262626"/>

      <rect x="206" y="102" width="327" height="85" fill="var(--gold)"/>
      <rect x="163" y="186" width="370" height="93" fill="var(--gold)"/>
      <rect x="253" y="279" width="280" height="79" fill="var(--gold)"/>

      <polygon points="306,54.5 533,54.5 533,96 306,96 285,75" fill="var(--ink)"/>
      <text class="author" x="490" y="87" text-anchor="end">MABEL JOY CRANE</text>

      <text class="title" x="492" y="180" text-anchor="end" font-size="85">FITNESS</text>
      <text class="title" x="492" y="263" text-anchor="end" font-size="85">TRAINER</text>
      <text class="title title-xb" x="492" y="344" text-anchor="end" font-size="84"><tspan font-size="48" font-weight="700">for </tspan>MEN</text>

      <ellipse role="img" aria-label="Photo of a blonde woman in a white bikini rising from a pool" cx="437" cy="505" rx="70" ry="135" fill="url(#bather-tone)"/>

      <text class="script" x="184" y="506" text-anchor="middle" font-size="24" fill="var(--white)" textLength="168" lengthAdjust="spacingAndGlyphs" transform="rotate(-20 184 498)">Helping Guys Get</text>
      <text class="script" x="192" y="543" text-anchor="middle" font-size="34" fill="var(--gold)" textLength="282" lengthAdjust="spacingAndGlyphs" transform="rotate(-20 192 531)">Hot, Sweaty, &amp; Hard</text>

      <text class="benefit" x="315" y="619" text-anchor="end">so Pounds Melt Away,</text>
      <text class="benefit" x="315" y="646" text-anchor="end">Your Gut Shrinks,</text>
      <text class="benefit" x="319" y="673" text-anchor="end">&amp; You Last Longer.</text>

      <ellipse role="img" aria-label="Black iron dumbbell" cx="105" cy="703" rx="64" ry="36" fill="url(#iron-tone)"/>
      <ellipse role="img" aria-label="Stack of iron weight plates" cx="437" cy="698" rx="62" ry="36" fill="url(#iron-tone)"/>

      <text class="benefit" x="268" y="752" text-anchor="middle">VOLUME II</text>
    </svg>
  </section>

</main>
</body>
</html>
```